Northway Trade Partners Needs a FRESH website

We would like a creative minded designer to take on the task to Re-design our website. Its a simple 5-7 pages. With no cart, no complex html. Just plain information about our company and products we import and export. Pictures added to the product section. Since Our logo its Blue, we would like the designer to use complementing colors in order to make the website look cleaner and modern.

Target Market(s)

The target audience will be companies looking to purchase plastic related products. Companies looking to purchase large quantities of plastic containers (Shampoo bottles, caps, sprayers, mist sprayers, cosmetic containers etc).

Industry/Entity Type

It Company

Font styles to use
Sans Serif

Requirements
Must have
• We have a section in which we would like to add pictures of some of the products we carry, therefore having an easy and clean way to navigate through the pictures will be a plus.

```html
<!DOCTYPE html>
<html lang="en">
<head>
<meta charset="utf-8">
<title>Northway Trade Partners</title>
<link href="https://fonts.googleapis.com/css2?family=Open+Sans:wght@300;400;600;700&display=swap" rel="stylesheet">
<style>
:root{
  --blue:#0f8fd6;
  --blue-light:#21a9ec;
  --blue-dark:#0a6cb3;
  --footer:#0b5cae;
  --ink:#444;
  --muted:#8a8a8a;
  --line:#c9c9c9;
  --white:#fff;
}
*{box-sizing:border-box;margin:0;padding:0}
html,body{width:1200px;height:1112px;overflow:hidden;background:var(--white);font-family:"Open Sans",Arial,sans-serif;color:var(--ink)}
.page{position:relative;width:1200px;height:1112px}
.brand{position:absolute;left:110px;top:14px;display:flex;align-items:center;gap:10px}
.brand-mark{width:72px;height:72px;border-radius:50%;background:var(--blue)}
.brand-name{font-size:23px;font-weight:400;color:var(--blue)}
.contact{position:absolute;right:110px;top:34px;text-align:right;font-size:14px;line-height:21px;color:#333}
.contact div{display:flex;justify-content:flex-end;align-items:center;gap:18px}
.contact svg{fill:#555}
.nav{position:absolute;left:110px;top:103px;width:980px;height:44px;border-radius:3px;background:linear-gradient(#1590d6,#0a69b0);display:flex}
.nav a{height:44px;display:flex;align-items:center;justify-content:center;color:var(--white);font-size:13px;text-decoration:none;border-right:1px solid #075a99}
.nav a.active{background:var(--blue-light)}
.search{position:absolute;right:6px;top:11px;display:flex;gap:5px}
.search-field{width:179px;height:23px;border-radius:3px;background:#e6e6e6;font-size:12px;color:#777;padding:3px 9px}
.search-btn{width:42px;height:23px;border-radius:3px;background:#e2e2e2;display:flex;align-items:center;justify-content:center}
.hero{position:absolute;left:110px;top:158px;width:980px;height:332px;border-radius:6px;overflow:hidden;background:radial-gradient(ellipse at 60% 45%,#c7d5e2 0%,#7f99b2 35%,#2c3f55 75%,#17222f 100%)}
.hero-box{position:absolute;left:15px;top:65px;width:358px;height:191px;background:rgba(30,30,30,.55);padding:6px 12px 0}
.hero-title{font-size:24px;font-weight:600;color:var(--white);line-height:40px;white-space:nowrap}
.hero-text{margin-top:8px;font-size:14px;line-height:24px;color:#eee;font-weight:300}
.btn{display:table;margin-top:20px;background:var(--blue);color:var(--white);font-size:14px;line-height:19px;padding:5px 10px;border-radius:3px;border:1px solid #3ab4f0}
.welcome-img{position:absolute;left:111px;top:534px;width:178px;height:114px;border:1px solid var(--line);border-radius:4px;background:linear-gradient(135deg,#f5f8fb,#6fa8dd 60%,#1d4f9c)}
.welcome{position:absolute;left:318px;top:527px;width:712px}
.welcome h1{font-size:25px;font-weight:400;color:#444;line-height:34px}
.welcome p{margin-top:9px;font-size:12.5px;line-height:24px;color:var(--muted);font-weight:300}
.welcome h1 span{color:var(--blue)}
.card{position:absolute;width:238px;height:137px;border:1px solid var(--line);border-radius:4px;padding:8px 9px}
.card h2{font-size:15px;font-weight:400;color:#444;line-height:20px}
.card-img{margin-top:6px;width:220px;height:83px;border:1px solid #ddd;border-radius:4px}
.footer{position:absolute;left:110px;top:1065px;width:980px;height:47px;background:var(--footer);display:flex;align-items:center;color:var(--white);font-size:12px}
.social{display:flex;gap:5px;margin-left:30px}
.social span{width:20px;height:20px;border-radius:3px;background:#6fa7db}
.footer-links{display:flex;margin-left:3px;font-weight:600}
.footer-links a{color:var(--white);text-decoration:none;padding:0 10px;border-right:2px solid var(--white);line-height:16px}
.footer-links a:last-child{border:none}
.copy{margin-left:auto;margin-right:7px;font-size:13px}
</style>
</head>
<body>
<div class="page">
  <header>
    <div class="brand"><div class="brand-mark"></div><div class="brand-name">Northway Trade Partners</div></div>
    <div class="contact">
      <div><svg width="14" height="14" viewBox="0 0 24 24"><path d="M6.6 10.8a15 15 0 0 0 6.6 6.6l2.2-2.2a1 1 0 0 1 1-.3 11 11 0 0 0 3.6.6 1 1 0 0 1 1 1V20a1 1 0 0 1-1 1A17 17 0 0 1 3 4a1 1 0 0 1 1-1h3.5a1 1 0 0 1 1 1 11 11 0 0 0 .6 3.6 1 1 0 0 1-.3 1z"/></svg><span>123 465 7890</span></div>
      <div><svg width="14" height="11" viewBox="0 0 14 11"><path d="M0 0h14v2L7 6 0 2z M0 4l7 4 7-4v7H0z"/></svg><span>info@northwaytrade.net</span></div>
    </div>
  </header>

  <nav class="nav">
    <a class="active" href="#" style="width:96px">HOME</a>
    <a href="#" style="width:111px">ABOUT US</a>
    <a href="#" style="width:128px">PRODUCTS</a>
    <a href="#" style="width:170px">MISSION STATEMENT</a>
    <a href="#" style="width:139px">CONTACT US</a>
    <div class="search">
      <div class="search-field">Search...</div>
      <div class="search-btn"><svg width="14" height="14" viewBox="0 0 14 14"><circle cx="6" cy="6" r="4.5" fill="none" stroke="#888" stroke-width="1.6"/><path d="M9.3 9.3 13 13" stroke="#888" stroke-width="1.8"/></svg></div>
    </div>
  </nav>

  <section class="hero" role="img" aria-label="Hands holding a world map connected by trade routes and arrows">
    <div class="hero-box">
      <div class="hero-title">Northway Trade Partners</div>
      <p class="hero-text">Lorem ipsum dolor sit amet, consectetuer adipiscing elit, sed diam nonummy nibh euismod tincidunt ut laoreet dolore magna aliquam erat volutpat.</p>
      <span class="btn">Read More</span>
    </div>
  </section>

  <div class="welcome-img" role="img" aria-label="Cargo plane, truck and globe with boxes"></div>
  <section class="welcome">
    <h1>Welcome To <span>Northway Trade Partners</span></h1>
    <p>Northway Trade Partners will be your first and last stop for sourcing products from all over the world, specifically Asia and South America. We have partners all around the globe that helps us make the best decision in sourcing a product from and to any market.</p>
  </section>

  <div class="card" style="left:109px;top:700px"><h2>Product Research</h2><div class="card-img" role="img" aria-label="Bar chart with magnifying glass" style="background:linear-gradient(#fff,#eef1f4)"></div></div>
  <div class="card" style="left:355px;top:700px"><h2>OEM/ODM</h2><div class="card-img" role="img" aria-label="Colourful plastic pellets" style="background:linear-gradient(#cfd6dc,#e6eaee 45%,#f08a2c 75%,#2b7fd6)"></div></div>
  <div class="card" style="left:603px;top:700px"><h2>Delivery</h2><div class="card-img" role="img" aria-label="Delivery truck with courier and parcels" style="background:linear-gradient(#fff,#c9ced4 60%,#f4f4f4)"></div></div>
  <div class="card" style="left:851px;top:700px"><h2>Freight Forwarding</h2><div class="card-img" role="img" aria-label="Globe with cargo ship and truck" style="background:linear-gradient(135deg,#5fa0d8,#1f4f86 60%,#c8cfd6)"></div></div>

  <div class="card" style="left:109px;top:880px"><h2>Packaging</h2><div class="card-img" role="img" aria-label="Cardboard packaging boxes" style="background:linear-gradient(#e9e6e1,#c6a27a 60%,#a77a4d)"></div></div>
  <div class="card" style="left:355px;top:880px"><h2>Product Designing</h2><div class="card-img" role="img" aria-label="Calipers on a technical drawing" style="background:linear-gradient(135deg,#f2f2f2,#cfd2d5 55%,#a9adb1)"></div></div>
  <div class="card" style="left:603px;top:880px"><h2>Labeling</h2><div class="card-img" role="img" aria-label="Hands applying a label" style="background:linear-gradient(135deg,#e0dfdc,#b9a596 55%,#6c5f58)"></div></div>
  <div class="card" style="left:851px;top:880px"><h2>Custom</h2><div class="card-img" role="img" aria-label="Globe surrounded by parcels" style="background:radial-gradient(circle at 50% 45%,#e2e4e6,#b48a5c 70%,#fff 71%)"></div></div>

  <footer class="footer">
    <div class="social"><span></span><span></span><span></span></div>
    <div class="footer-links"><a href="#">Home</a><a href="#">Sitemap</a><a href="#">Terms and conditions</a></div>
    <div class="copy">Copyright 2014. Northway Trade Partners. All rights reserved.</div>
  </footer>
</div>
</body>
</html>
```